Halvern Aviation Group - "Coming Soon" Main Company Webpage

Design a main webpage that can be posted while a fully functional website is constructed. The design should be created to convey a sense of luxury and exclusivity. The main page should contain only one photo as the background. The photo I believe to show "luxury" and "Exclusivity" is listed as "Global Luxury Photo". I have included two other photos as well to aid in providing a variety of presentations.
The "Member PQTR" logo should appear somewhere on the main page but be less prevalent than the main company logo. "Coming Soon" should also appear to convey that a website is being constructed.
Tabs for the website:
- Aircraft Management
- Aircraft Sales
- Pilot Services
- Charter
- Flight Training

```html
<!DOCTYPE html>
<html lang="en">
<head>
<meta charset="utf-8">
<title>Halvern Aviation Group — Coming Soon</title>
<link rel="stylesheet" href="https://fonts.googleapis.com/css2?family=Russo+One&family=Space+Grotesk:wght@400;500;700&display=swap">
<style>
  :root {
    --brand-blue: #0b5cb1;
    --ink: #14171c;
    --sky-light: #eceded;
    --sky-mid: #d6d8da;
    --sky-dark: #b9bcc0;
    --white: #ffffff;
  }
  * { margin: 0; padding: 0; box-sizing: border-box; }
  html, body { width: 1200px; height: 799px; overflow: hidden; }
  body { font-family: "Space Grotesk", sans-serif; color: var(--ink); }

  .page {
    position: relative;
    width: 1200px;
    height: 799px;
    overflow: hidden;
  }
  .hero-photo {
    position: absolute;
    inset: 0;
    background:
      radial-gradient(ellipse 60% 45% at 78% 78%, #f3f4f5 0%, rgba(243,244,245,0) 70%),
      radial-gradient(ellipse 70% 60% at 30% 30%, var(--sky-light) 0%, rgba(236,237,237,0) 70%),
      linear-gradient(180deg, var(--sky-mid) 0%, var(--sky-light) 40%, var(--sky-mid) 75%, var(--sky-dark) 100%);
  }

  .brand {
    position: absolute;
    left: 83px;
    top: 38px;
    font-weight: 700;
    font-size: 17px;
    letter-spacing: 0.5px;
    color: var(--brand-blue);
    text-transform: uppercase;
  }

  .main-nav {
    position: absolute;
    top: 39px;
    left: 356px;
    width: 762px;
    height: 22px;
  }
  .main-nav a {
    position: absolute;
    top: 0;
    height: 22px;
    line-height: 22px;
    font-size: 9.5px;
    font-weight: 700;
    letter-spacing: 1.1px;
    text-transform: uppercase;
    text-decoration: none;
    color: var(--ink);
    white-space: nowrap;
  }
  .main-nav .nav-active {
    left: 0;
    width: 108px;
    border: 1px solid var(--ink);
    text-align: center;
  }
  .main-nav .nav-pointer { position: absolute; left: 108px; top: 5px; }
  .main-nav .nav-management { left: 242px; }
  .main-nav .nav-management svg { margin-left: 3px; vertical-align: middle; }
  .main-nav .nav-pilot { left: 435px; }
  .main-nav .nav-charter { left: 570px; }
  .main-nav .nav-training { right: 0; }

  .hero-plane-cutout {
    position: absolute;
    left: 787px;
    top: 136px;
    width: 250px;
    height: 95px;
    border-radius: 50% 50% 40% 40%;
    background: linear-gradient(135deg, #c9b59a 0%, #a7a39a 50%, #8f8f8c 100%);
    opacity: 0.55;
  }

  .hero-copy {
    position: absolute;
    right: 82px;
    top: 248px;
    width: 640px;
    text-align: right;
  }
  .hero-title {
    font-family: "Russo One", sans-serif;
    font-weight: 400;
    font-size: 58px;
    letter-spacing: 1.5px;
    line-height: 1;
    color: var(--brand-blue);
  }
  .hero-text {
    margin-top: 40px;
    font-size: 16.2px;
    line-height: 24.3px;
    letter-spacing: 1px;
    color: var(--ink);
  }
  .cta-button {
    display: inline-block;
    margin-top: 33px;
    width: 146px;
    height: 42px;
    line-height: 42px;
    border-radius: 5px;
    background: var(--brand-blue);
    color: var(--white);
    font-size: 10.8px;
    font-weight: 700;
    letter-spacing: 1px;
    text-transform: uppercase;
    text-align: center;
    text-decoration: none;
  }

  .membership {
    position: absolute;
    left: 83px;
    top: 711px;
  }
  .membership-label {
    display: block;
    margin-left: 46px;
    font-size: 9px;
    color: var(--ink);
  }
  .membership-mark {
    display: flex;
    align-items: center;
    gap: 9px;
  }
  .membership-dot {
    width: 37px;
    height: 26px;
    border-radius: 50%;
    background: var(--brand-blue);
  }
  .membership-name {
    font-size: 26px;
    font-weight: 500;
    letter-spacing: 2px;
    color: var(--ink);
  }

  .menu-toggle {
    position: absolute;
    left: 1075px;
    top: 717px;
  }
</style>
</head>
<body>
<main class="page">
  <div class="hero-photo" role="img" aria-label="Private jet wing and engine against an overcast sky"></div>

  <div class="brand">Halvern Aviation Group</div>

  <nav class="main-nav">
    <a class="nav-active" href="#">Aircraft Sales</a>
    <svg class="nav-pointer" width="86" height="12" viewBox="0 0 86 12" aria-hidden="true">
      <line x1="0" y1="6" x2="84" y2="6" stroke="#14171c" stroke-width="1"/>
      <path d="M78 2 L85 6 L78 10" fill="none" stroke="#14171c" stroke-width="1"/>
    </svg>
    <a class="nav-management" href="#">Aircraft Management<svg width="6" height="4" viewBox="0 0 6 4" aria-hidden="true"><path d="M0.5 0.5 L3 3 L5.5 0.5" fill="none" stroke="#14171c" stroke-width="1.2"/></svg></a>
    <a class="nav-pilot" href="#">Pilot Services</a>
    <a class="nav-charter" href="#">Charter</a>
    <a class="nav-training" href="#">Flight Training</a>
  </nav>

  <div class="hero-plane-cutout" role="img" aria-label="Aircraft silhouette filled with a sunlit cloud photograph"></div>

  <section class="hero-copy">
    <h1 class="hero-title">COMING SOON</h1>
    <p class="hero-text">Lorem Ipsum Is Simply Dummy Text Of The Printing And Typesetting Industry. Lorem Ipsum Has Been The Industry’s Standard Dummy Text Ever Since The 1500s, When An Unknown Printer Took A Galley Of Type And Scrambled It To Make A Type Specimen Book. It Has Survived Not Only Five Centuries, But Also The Leap Into Electronic Typesetting, Remaining Essentially Unchanged. It Was Popularised In The 1960s With The Release Of Letraset Sheets Containing Lorem Ipsum Passages, And More Recently With Desktop Publishing Software Like Aldus PageMaker Including Versions Of Lorem Ipsum.</p>
    <a class="cta-button" href="#">Schedule a Call</a>
  </section>

  <div class="membership">
    <span class="membership-label">member of</span>
    <div class="membership-mark">
      <span class="membership-dot"></span>
      <span class="membership-name">PQTR</span>
    </div>
  </div>

  <svg class="menu-toggle" width="43" height="29" viewBox="0 0 43 29" aria-label="Menu">
    <line x1="0" y1="1.5" x2="43" y2="1.5" stroke="#14171c" stroke-width="2.5"/>
    <line x1="14" y1="14.5" x2="43" y2="14.5" stroke="#14171c" stroke-width="2.5"/>
    <line x1="0" y1="27.5" x2="43" y2="27.5" stroke="#14171c" stroke-width="2.5"/>
  </svg>
</main>
</body>
</html>
```